Branvique needs a business Card Design

We are looking for a business card Design for our new Managed Service Provider Company, Branvique. Branvique encompasses everything IT for the average medium sized business. Our primary services are help desk support, cyber-security (malware and ransomware protection), and Disaster Recovery systems. We would like the design to have a very clean and professional look, with a very minimalist feel.

Target Market(s)

Medium to large sized businesses

Industry/Entity Type

It Service

Contact Information for Business Card

Name GoesHere
name@branvique.com
O: 555-382-6047
C: 555-731-5820

Font styles to use
Other font styles liked:
• Poppins Font Only Please

Colors

Designer to choose only greyscale colors for use in the design.

Requirements
Must have
• Logo included
Nice to have
• Cutting Edge, innovative, minimalistic, elegant

```html
<!DOCTYPE html>
<html lang="en">
<head>
<meta charset="utf-8">
<title>Branvique Business Card</title>
<link href="https://fonts.googleapis.com/css2?family=Poppins:wght@300;400;500&display=swap" rel="stylesheet">
<style>
  :root {
    --page-bg: #2a2a2a;
    --card-deep: #1c1c1c;
    --card-light: #363636;
    --ink: #ffffff;
    --ink-soft: #e4e4e4;
  }
  * { margin: 0; padding: 0; box-sizing: border-box; }
  html, body {
    width: 1200px; height: 900px; overflow: hidden;
    background: var(--page-bg);
    font-family: "Poppins", sans-serif;
    color: var(--ink);
  }
  .card {
    position: absolute;
    left: 290px;
    width: 620px;
    height: 354px;
    background: linear-gradient(135deg, var(--card-deep) 0%, var(--card-deep) 45%, var(--card-light) 100%);
    box-shadow: 0 12px 30px rgba(0,0,0,0.5);
  }
  .card-front { top: 70px; }
  .card-back { top: 470px; }

  .brand-mark {
    position: absolute;
    left: 50%;
    top: 96px;
    width: 56px;
    height: 56px;
    margin-left: -28px;
    border: 3px solid var(--ink);
  }
  .brand {
    position: absolute;
    left: 0; right: 0; top: 178px;
    text-align: center;
    font-weight: 400;
    font-size: 34px;
    letter-spacing: 0.42em;
    padding-left: 0.42em;
    text-transform: uppercase;
  }

  .identity {
    position: absolute;
    right: 346px;
    top: 122px;
    text-align: right;
  }
  .identity-name {
    font-weight: 500;
    font-size: 31px;
    letter-spacing: 0.04em;
    text-transform: uppercase;
    line-height: 1.15;
    white-space: nowrap;
  }
  .identity-role {
    font-weight: 300;
    font-size: 18px;
    color: var(--ink-soft);
  }
  .divider {
    position: absolute;
    left: 298px;
    top: 118px;
    width: 1px;
    height: 96px;
    background: var(--ink);
  }
  .contact-list {
    position: absolute;
    left: 318px;
    top: 112px;
    list-style: none;
  }
  .contact-list li {
    display: flex;
    align-items: center;
    gap: 9px;
    font-weight: 300;
    font-size: 18px;
    letter-spacing: 0.04em;
    line-height: 27px;
    white-space: nowrap;
  }
  .contact-list svg { width: 12px; height: 12px; flex: none; }
  .address {
    position: absolute;
    left: 0; right: 0; bottom: 34px;
    text-align: center;
    font-weight: 300;
    font-size: 18px;
    letter-spacing: 0.05em;
  }
</style>
</head>
<body>
  <section class="card card-front">
    <div class="brand-mark" aria-hidden="true"></div>
    <div class="brand">Branvique</div>
  </section>

  <section class="card card-back">
    <div class="identity">
      <div class="identity-name">Daniel Reyes</div>
      <div class="identity-role">Director</div>
    </div>
    <div class="divider"></div>
    <ul class="contact-list">
      <li>
        <svg viewBox="0 0 12 12" aria-hidden="true"><path d="M2.5 1 L4.5 1 L5 3.5 L3.8 4.4 Q5 7 7.6 8.2 L8.5 7 L11 7.5 L11 9.5 Q11 11 9.5 11 Q1 10 1 2.5 Q1 1 2.5 1 Z" fill="currentColor"/></svg>
        555-382-6047
      </li>
      <li>
        <svg viewBox="0 0 12 12" aria-hidden="true"><rect x="3" y="0.8" width="6" height="10.4" rx="1" fill="none" stroke="currentColor" stroke-width="1.2"/><circle cx="6" cy="9.3" r="0.7" fill="currentColor"/></svg>
        555-731-5820
      </li>
      <li>
        <svg viewBox="0 0 12 12" aria-hidden="true"><rect x="0.8" y="2.3" width="10.4" height="7.4" fill="none" stroke="currentColor" stroke-width="1.1"/><path d="M0.8 2.5 L6 6.5 L11.2 2.5" fill="none" stroke="currentColor" stroke-width="1.1"/></svg>
        daniel@branvique.com
      </li>
      <li>
        <svg viewBox="0 0 12 12" aria-hidden="true"><g fill="none" stroke="currentColor" stroke-width="0.9"><circle cx="6" cy="6" r="5"/><ellipse cx="6" cy="6" rx="2.2" ry="5"/><path d="M1 6 H11 M2 3.3 H10 M2 8.7 H10"/></g></svg>
        www.danielbranvique.com
      </li>
    </ul>
    <div class="address">48 Calder Lane Riverton, TN 37120</div>
  </section>
</body>
</html>
```